Painting Company Business Card

Brightwell Painting needs a new business card. See attachments for our logo and current card as an example.
We want to utilize the same colors in the logo, and keep all the information that is currently on it. Just need an updated and modern design.
We are open to loosing the Association Logos if it means a better design.
We are also entertaining a spot for a picture of a headshot of the person listed on the card. Head shot can be finished later.

```html
<!DOCTYPE html>
<html lang="en">
<head>
<meta charset="utf-8">
<title>Brightwell Painting – Business Card</title>
<link href="https://fonts.googleapis.com/css2?family=Oswald:wght@400;500&family=Roboto:wght@700&display=swap" rel="stylesheet">
<style>
  :root {
    --page-bg: #e2e2e2;
    --card-bg: #d9d9d7;
    --brand-green: #2f5226;
    --brand-green-dark: #2a3b23;
    --band-text: #e9ece6;
    --ink: #2b2b2b;
    --badge: #dfe3dc;
    --frame: #1e1e1e;
  }
  * { box-sizing: border-box; margin: 0; padding: 0; }
  html, body { width: 1200px; height: 1200px; overflow: hidden; }
  body {
    background: var(--page-bg);
    font-family: "Oswald", "Arial Narrow", sans-serif;
    position: relative;
  }
  .card {
    position: absolute;
    left: 160px;
    width: 880px;
    height: 500px;
    background: var(--card-bg);
    box-shadow: 0 6px 18px rgba(0,0,0,0.18);
    overflow: hidden;
  }
  .card--front { top: 70px; }
  .card--back { top: 630px; }

  .paint-band { position: absolute; top: 0; height: 500px; }
  .card--front .paint-band { left: 490px; width: 300px; }
  .card--back .paint-band { left: 30px; width: 380px; }

  /* Front */
  .brand-mark {
    position: absolute;
    left: 60px;
    top: 120px;
    display: flex;
    align-items: center;
    gap: 18px;
  }
  .brand-mark__square {
    width: 40px; height: 40px;
    background: var(--brand-green-dark);
  }
  .brand-mark__name {
    font-weight: 500;
    font-size: 62px;
    line-height: 1.05;
    color: var(--brand-green-dark);
    text-transform: uppercase;
    letter-spacing: 1px;
  }
  .services {
    position: absolute;
    left: 520px;
    top: 50px;
    width: 240px;
    text-align: center;
    color: var(--band-text);
    font-size: 23px;
    line-height: 1.2;
    letter-spacing: 1.5px;
    text-transform: uppercase;
  }
  .band-rule {
    position: absolute;
    height: 2px;
    background: var(--band-text);
    opacity: 0.8;
  }
  .card--front .band-rule { left: 560px; top: 215px; width: 170px; }
  .card--back .band-rule { left: 80px; top: 265px; width: 270px; }
  .badges {
    position: absolute;
    left: 515px;
    top: 270px;
    width: 250px;
    display: grid;
    grid-template-columns: repeat(3, 1fr);
    gap: 22px 14px;
    justify-items: center;
    align-items: center;
  }
  .badge { background: var(--badge); opacity: 0.85; }
  .badge--tall { width: 36px; height: 54px; }
  .badge--wide { width: 78px; height: 36px; border-radius: 4px; }
  .badge--round { width: 46px; height: 46px; border-radius: 50%; }

  /* Back */
  .contact-list {
    position: absolute;
    left: 70px;
    top: 60px;
    list-style: none;
    color: var(--band-text);
    font-size: 21px;
    letter-spacing: 0.5px;
  }
  .contact-list li {
    display: flex;
    align-items: center;
    gap: 14px;
    height: 44px;
  }
  .contact-list svg { width: 24px; height: 24px; flex: none; }
  .back-mark {
    position: absolute;
    left: 80px;
    top: 320px;
    display: flex;
    align-items: center;
    gap: 10px;
    color: var(--band-text);
    font-weight: 500;
    font-size: 24px;
    line-height: 1.05;
    text-transform: uppercase;
  }
  .back-mark__square { width: 18px; height: 18px; background: var(--band-text); }
  .address {
    position: absolute;
    left: 80px;
    top: 400px;
    display: flex;
    gap: 10px;
    color: var(--band-text);
    font-size: 20px;
    line-height: 1.3;
  }
  .address svg { width: 20px; height: 26px; flex: none; margin-top: 2px; }
  .headshot-frame {
    position: absolute;
    left: 540px;
    top: 28px;
    width: 230px;
    height: 240px;
    background: var(--frame);
    padding: 30px;
    box-shadow: 0 4px 10px rgba(0,0,0,0.3);
  }
  .headshot {
    width: 100%; height: 100%;
    background: linear-gradient(180deg, #f4f4f4 0%, #cfcfcf 55%, #1c1c1c 100%);
    border: 1px solid #6b5a2c;
  }
  .person {
    position: absolute;
    right: 45px;
    top: 290px;
    text-align: right;
  }
  .person__name {
    font-family: "Roboto", "Helvetica", sans-serif;
    font-weight: 700;
    font-size: 30px;
    color: var(--brand-green-dark);
  }
  .person__title {
    font-size: 21px;
    letter-spacing: 3px;
    color: var(--ink);
    text-transform: uppercase;
  }
</style>
</head>
<body>

<section class="card card--front" aria-label="Business card front">
  <svg class="paint-band" viewBox="0 0 300 500" preserveAspectRatio="none" aria-hidden="true">
    <path fill="var(--brand-green)" d="M22 0 L282 0 L276 30 L288 62 L279 95 L290 130 L280 168 L287 205 L277 240 L289 278 L281 315 L290 350 L278 388 L287 425 L280 462 L286 500 L14 500 L22 468 L10 432 L20 396 L8 360 L19 322 L11 288 L22 250 L9 214 L18 178 L8 140 L20 104 L10 70 L19 36 Z"/>
  </svg>

  <div class="brand-mark">
    <span class="brand-mark__square"></span>
    <span class="brand-mark__name">Brightwell<br>Painting</span>
  </div>

  <div class="services">
    Exterior Paiting<br>Interior Painting<br>Carpentry<br>Drywall
  </div>
  <div class="band-rule"></div>

  <div class="badges" aria-label="Association memberships">
    <span class="badge badge--tall"></span>
    <span class="badge badge--wide"></span>
    <span class="badge badge--round"></span>
    <span class="badge badge--wide"></span>
    <span class="badge badge--round"></span>
    <span class="badge badge--tall"></span>
  </div>
</section>

<section class="card card--back" aria-label="Business card back">
  <svg class="paint-band" viewBox="0 0 380 500" preserveAspectRatio="none" aria-hidden="true">
    <path fill="var(--brand-green)" d="M18 0 L362 0 L356 34 L370 70 L358 108 L372 146 L360 184 L369 222 L357 260 L371 298 L359 336 L370 374 L358 412 L368 450 L360 500 L14 500 L24 462 L10 426 L20 388 L8 350 L21 312 L11 274 L23 236 L9 198 L19 160 L8 122 L22 84 L10 46 Z"/>
  </svg>

  <ul class="contact-list">
    <li>
      <svg viewBox="0 0 24 24" aria-hidden="true"><rect x="6" y="1.5" width="12" height="21" rx="2" fill="none" stroke="currentColor" stroke-width="1.8"/><line x1="10" y1="19" x2="14" y2="19" stroke="currentColor" stroke-width="1.8"/></svg>
      <span>555-014-2290</span>
    </li>
    <li>
      <svg viewBox="0 0 24 24" aria-hidden="true"><rect x="2" y="5" width="20" height="14" fill="currentColor"/><path d="M2 5 L12 13 L22 5" fill="none" stroke="var(--brand-green)" stroke-width="1.8"/></svg>
      <span>Daniel@brightwellmail.com</span>
    </li>
    <li>
      <svg viewBox="0 0 24 24" aria-hidden="true"><circle cx="11" cy="11" r="9" fill="none" stroke="currentColor" stroke-width="1.8"/><ellipse cx="11" cy="11" rx="4" ry="9" fill="none" stroke="currentColor" stroke-width="1.5"/><line x1="2" y1="11" x2="20" y2="11" stroke="currentColor" stroke-width="1.5"/><path d="M15 15 L22 18 L19 19 L18 22 Z" fill="currentColor"/></svg>
      <span>BrightwellPainting.com</span>
    </li>
  </ul>
  <div class="band-rule"></div>

  <div class="back-mark">
    <span class="back-mark__square"></span>
    <span>Brightwell<br>Painting</span>
  </div>

  <div class="address">
    <svg viewBox="0 0 20 26" aria-hidden="true"><path d="M10 1 C4.5 1 1 5 1 9.5 C1 16 10 25 10 25 C10 25 19 16 19 9.5 C19 5 15.5 1 10 1 Z" fill="currentColor"/><circle cx="10" cy="9.5" r="3.5" fill="var(--brand-green)"/></svg>
    <span>48 Alder Lane #2,<br>Millbrook, WI 53090</span>
  </div>

  <div class="headshot-frame">
    <div class="headshot" role="img" aria-label="Headshot photo of Daniel Hart"></div>
  </div>

  <div class="person">
    <div class="person__name">Daniel Hart</div>
    <div class="person__title">Quality Manager</div>
  </div>
</section>

</body>
</html>
```